Luxury Wine Label for New Startup Winery

We need a wine label for our new winery startup. We have worked with a local designer but do not feel the resulting label / logo have the elevation required to present our brand as a luxury wine. Our winery is called "Harrowgate Vineyards" and we are focused on extremely high quality hand crafted artisan and estate wines from the Pacific Northwest.
We would like to see designs that utilize a tree line, or other imagery that represents the "Harrowgate" part of our company name. Another interesting feature could be wood grain.
A logo will be required based on your design so please design with this in mind:
This logo should be consistent with the wine bottle label design, and should be representative of our high end exclusive wine while giving a sense of place (Oregon/ Pacific Northwest.)
I will supply an image of the design we received from our local designer, PLEASE NOTE: in general we do like wood grain and tree line concepts but feel the execution was poorly done.
ATTN: Logo design should be suitable for use on: Bottles (Red wine/rose/white wine), Bussiness cards, vehicle signage, business signage, etc
P.S.:
If you have a design that is not outside the box we are still interested in seeing it.
Label is for a burgundy style bottle with a label height of 3.5 - 4" and a width of 3.5-4"
any label <= 4"x4" and >=3.5"x3.5" will be acceptable:
HOWEVER Width should be greater than or equal to height due to the bottle format
Target Market(s)
Wine enthusiasts with adequate discretionary budgets to afford $100 bottles of wine.
Industry/Entity Type
Wine / Winery
Requirements
Must have
- A sense of luxury, a feel of exclusivity, and a theme consistent with our product and brand name
Nice to have
- Tree line, wood grain or other wood themes. Serif fonts
Should not have
- anything cheesy, off topic, hard to read script fonts or anything that makes the label hard to read from a few feet away or too busy

```html
<!DOCTYPE html>
<html lang="en">
<head>
<meta charset="utf-8">
<title>Harrowgate Vineyards – Syrah Label</title>
<link href="https://fonts.googleapis.com/css2?family=Cinzel:wght@500&family=Montserrat:wght@500;600&display=swap" rel="stylesheet">
<style>
  :root {
    --backdrop: #e9e4e4;
    --wood-deep: #2e1108;
    --wood-dark: #43190b;
    --wood-mid: #5e2510;
    --wood-warm: #7a3616;
    --gold: #d9a35f;
    --cream: #f3e6d6;
  }
  * { margin: 0; padding: 0; box-sizing: border-box; }
  html, body {
    width: 880px;
    height: 1200px;
    overflow: hidden;
    background: var(--backdrop);
  }
  .canvas {
    position: relative;
    width: 880px;
    height: 1200px;
  }
  .label {
    position: absolute;
    left: 50px;
    top: 220px;
    width: 780px;
    height: 760px;
    overflow: hidden;
    box-shadow: 0 12px 40px rgba(40, 15, 5, 0.25);
  }
  .label__grain {
    position: absolute;
    inset: 0;
    background:
      radial-gradient(ellipse 60% 40% at 25% 15%, var(--wood-warm) 0%, transparent 70%),
      radial-gradient(ellipse 50% 60% at 85% 55%, var(--wood-warm) 0%, transparent 70%),
      radial-gradient(ellipse 45% 35% at 15% 75%, var(--wood-deep) 0%, transparent 70%),
      radial-gradient(ellipse 55% 30% at 60% 95%, var(--wood-deep) 0%, transparent 70%),
      linear-gradient(165deg, var(--wood-mid) 0%, var(--wood-dark) 50%, var(--wood-mid) 100%);
  }
  .brand {
    position: absolute;
    top: 50px;
    left: 50%;
    transform: translateX(-50%);
    width: 200px;
    height: 200px;
    display: flex;
    align-items: center;
    justify-content: center;
  }
  .brand__ring {
    position: absolute;
    inset: 0;
  }
  .brand__name {
    position: relative;
    font-family: "Montserrat", sans-serif;
    font-weight: 600;
    font-size: 20px;
    line-height: 1.35;
    letter-spacing: 0.06em;
    text-transform: uppercase;
    text-align: center;
    color: var(--gold);
  }
  .varietal {
    position: absolute;
    top: 330px;
    width: 100%;
    text-align: center;
    font-family: "Cinzel", serif;
    font-weight: 500;
    font-size: 100px;
    line-height: 1.2;
    letter-spacing: 0.02em;
    color: var(--gold);
  }
  .details {
    position: absolute;
    top: 565px;
    width: 100%;
    text-align: center;
    font-family: "Montserrat", sans-serif;
    font-weight: 500;
    color: var(--cream);
    letter-spacing: 0.04em;
  }
  .details__vintage { font-size: 26px; margin-bottom: 16px; }
  .details__region { font-size: 28px; }
</style>
</head>
<body>
  <main class="canvas">
    <section class="label">
      <div class="label__grain" role="img" aria-label="Flowing dark walnut wood grain texture"></div>

      <div class="brand">
        <svg class="brand__ring" viewBox="0 0 200 200" aria-hidden="true">
          <circle cx="100" cy="100" r="95" fill="none" stroke="var(--gold)" stroke-width="3"/>
        </svg>
        <p class="brand__name">Harrowgate<br>Vineyards</p>
      </div>

      <h1 class="varietal">SYRAH</h1>

      <div class="details">
        <p class="details__vintage">2024</p>
        <p class="details__region">WILLAMETTE VALLEY</p>
      </div>
    </section>
  </main>
</body>
</html>
```